World Wide News and Current Affairs website

We intends to start up a new website which deals on New and Current Affairs.
Attention Designers,
We want a home page design for this project. Our business is based in the United States. Our goal is to become a well known brand.
The website would consist of a category for News, Business and Tech.
The theme should be beautiful and attention seeking. The website would take bulk of it's news from the US, and Europe.
Designers can get inspiration from already existing new websites such as HVZ, FQJ, DORNAKE.
All designs should be clean and easy to navigate.

```html
<!DOCTYPE html>
<html lang="en">
<head>
<meta charset="utf-8">
<title>Halvern News</title>
<link href="https://fonts.googleapis.com/css2?family=Raleway:wght@400;500;600;700&family=Open+Sans:wght@400;600&display=swap" rel="stylesheet">
<style>
:root{
  --ink:#222;
  --text:#555;
  --muted:#888;
  --dark:#1b1b1b;
  --panel:#161616;
  --grey-bg:#ebebeb;
  --white:#fff;
  --orange:#f7a21b;
  --red:#e8180c;
  --green:#3aa43a;
  --blue:#2a7fd4;
  --line:#e2e2e2;
}
*{box-sizing:border-box;margin:0;padding:0}
html,body{width:1200px;height:4752px;overflow:hidden}
body{position:relative;background:var(--white);font-family:"Open Sans",sans-serif;color:var(--ink)}
.band{position:absolute;left:0;width:1200px}
.grey{background:var(--grey-bg)}

/* nav */
.topbar{top:0;height:61px;background:var(--dark)}
.brand{position:absolute;left:162px;top:19px;font-family:"Raleway",sans-serif;font-weight:700;font-size:17px;letter-spacing:1px;color:var(--white)}
.menu{position:absolute;top:21px;font-family:"Raleway",sans-serif;font-size:13px;font-weight:500;color:var(--white)}
.menu.active{color:var(--orange)}
.search{position:absolute;left:846px;top:14px;width:192px;height:32px;background:var(--white);font-size:11px;font-style:italic;color:#999;padding:9px 10px}
.search svg{position:absolute;right:10px;top:9px}

/* photo placeholders */
.photo{position:absolute;background:linear-gradient(135deg,#8a8f96,#4a4f57)}
.photo.warm{background:linear-gradient(135deg,#c9a07a,#5b3f2d)}
.photo.cool{background:linear-gradient(135deg,#a9b6c4,#4c5b6d)}
.photo.light{background:linear-gradient(135deg,#e2e4e6,#9ba2a9)}
.photo.dark{background:linear-gradient(135deg,#5a5d62,#202226)}

.hero-title{position:absolute;left:195px;top:404px;font-family:"Raleway",sans-serif;font-weight:600;font-size:24px;color:var(--white)}
.hero-text{position:absolute;left:195px;top:440px;width:260px;font-size:10.5px;line-height:19px;color:#eee}
.hero-dots{position:absolute;left:562px;top:453px;display:flex;gap:8px}
.hero-dots span{width:28px;height:3px;background:var(--white)}
.side-caption{position:absolute;left:18px;bottom:22px;width:230px;font-size:12.5px;line-height:22px;color:var(--white)}

/* section headings */
.sec-head{position:absolute;left:160px;font-family:"Raleway",sans-serif;font-weight:700;font-size:21px;color:#333;border-left:4px solid var(--red);padding-left:7px;line-height:21px}
.sec-head.green{border-color:var(--green)}
.sec-head.orange{border-color:var(--orange)}
.sec-head.blue{border-color:var(--blue)}
.arrows{position:absolute;left:1004px;display:flex;gap:6px}
.rule{position:absolute;left:160px;width:878px;height:3px;background:var(--line)}

/* cards */
.row{position:absolute;left:160px;width:878px;display:flex;justify-content:space-between}
.card{width:277px;position:relative}
.row.four .card{width:205px}
.card .pic{position:relative;height:153px;background:linear-gradient(135deg,#9aa3ad,#4e5762)}
.card .pic.warm{background:linear-gradient(135deg,#c9a07a,#5b3f2d)}
.card .pic.light{background:linear-gradient(135deg,#e4e6e8,#9ca3aa)}
.card .pic.dark{background:linear-gradient(135deg,#5c6067,#1f2226)}
.card h3{margin-top:20px;font-family:"Raleway",sans-serif;font-weight:600;font-size:16px;color:#222}
.card p{margin-top:10px;font-size:10.5px;line-height:19px;color:var(--text)}
.btn{display:inline-block;margin-top:16px;border:1px solid #cfcfcf;font-size:11px;color:#666;padding:5px 11px}

/* lists */
.list-panel{position:absolute;background:var(--panel);color:var(--white)}
.list-panel .head{height:46px;padding:13px 15px;font-family:"Raleway",sans-serif;font-weight:600;font-size:15px;color:var(--white)}
.item{position:absolute;left:0;width:100%;display:flex;align-items:center;gap:16px;padding:0 15px;font-size:13px;line-height:21px}
.num{flex:none;width:32px;height:32px;border-radius:50%;display:flex;align-items:center;justify-content:center;font-size:11px;color:var(--white)}
.divider{position:absolute;left:0;width:100%;height:1px;background:#2e2e2e}

.play{position:absolute;width:72px;height:60px;background:#111;display:flex;align-items:center;justify-content:center}

/* more cards */
.mcard{width:205px;background:var(--white);height:287px}
.mcard .pic{height:154px}
.mcard .body{padding:0 20px}
.mcard h4{margin-top:20px;font-family:"Raleway",sans-serif;font-weight:600;font-size:14px}
.mcard p{margin-top:8px;font-size:10px;line-height:19px;color:var(--text)}
.tag{margin-top:10px;font-size:10px;font-weight:600;color:var(--green)}

/* featured list */
.feat-item{position:absolute;left:763px;width:275px;border-bottom:1px solid var(--line);padding-bottom:16px}
.feat-item h3{font-family:"Raleway",sans-serif;font-weight:600;font-size:16px}
.feat-item p{margin-top:10px;font-size:10.5px;line-height:19px;color:var(--text)}

/* footer */
.footer{top:4475px;height:277px;background:var(--dark);color:#ddd}
.f-head{position:absolute;top:44px;font-family:"Raleway",sans-serif;font-weight:700;font-size:12.5px;color:var(--white)}
.f-text{position:absolute;top:78px;font-size:10px;line-height:20px;color:#ccc}
.social{position:absolute;left:568px;top:78px;display:grid;grid-template-columns:repeat(3,26px);gap:6px}
.social span{width:26px;height:26px;background:var(--orange)}
.email{position:absolute;left:752px;top:125px;width:286px;height:41px;border:1px solid #555;font-size:10px;color:#ddd;padding:13px 10px}
.signup{position:absolute;right:-1px;top:-1px;width:82px;height:41px;background:var(--orange);color:var(--white);font-weight:600;font-size:10.5px;display:flex;align-items:center;justify-content:center}
.copy{position:absolute;top:229px;width:1200px;text-align:center;font-size:10px;color:#ccc}
</style>
</head>
<body>

<header class="band topbar">
  <div class="brand">HALVERN NEWS</div>
  <span class="menu active" style="left:407px">Home</span>
  <span class="menu" style="left:481px">About</span>
  <span class="menu" style="left:555px">News</span>
  <span class="menu" style="left:627px">Business</span>
  <span class="menu" style="left:718px">Tech</span>
  <span class="menu" style="left:786px">More</span>
  <div class="search">Search
    <svg width="12" height="12" viewBox="0 0 12 12"><circle cx="5" cy="5" r="3.8" fill="none" stroke="#222" stroke-width="1.6"/><line x1="8" y1="8" x2="11" y2="11" stroke="#222" stroke-width="1.8"/></svg>
  </div>
</header>

<section class="band grey" style="top:61px;height:488px"></section>
<div class="photo dark" style="left:160px;top:114px;width:568px;height:380px" role="img" aria-label="Person in jeans typing on a laptop with a tablet and coffee cup"></div>
<div class="hero-title">Halvern News</div>
<div class="hero-text">Lorem ipsum dolor sit amet, consectetur adipiscn elit, seddo eiusmod tempor incididuntit.</div>
<div class="hero-dots"><span></span><span></span><span></span><span></span></div>
<div class="photo dark" style="left:745px;top:114px;width:293px;height:182px" role="img" aria-label="Microphones held out at a press conference">
  <div class="side-caption">Lorem ipsum dolor sit aconse ctetu radicrssum dolor sum dolor.</div>
</div>
<div class="photo cool" style="left:745px;top:309px;width:293px;height:182px" role="img" aria-label="Business team in a meeting">
  <div class="side-caption">Lorem ipsum dolor sit aconse ctetu radicrssum dolor sum dolor.</div>
</div>

<h2 class="sec-head" style="top:594px">News</h2>
<div class="arrows" style="top:592px"><svg width="38" height="22" viewBox="0 0 38 22"><polyline points="12,3 4,11 12,19" fill="none" stroke="#999" stroke-width="2"/><polyline points="26,3 34,11 26,19" fill="none" stroke="#999" stroke-width="2"/></svg></div>
<div class="row" style="top:643px">
  <article class="card"><div class="pic warm" role="img" aria-label="Person reading on a tablet"></div><h3>Sed pesru lorem ismciatin</h3><p>Lorem ipsum dolor sit amet, consectetur adipiscn elit, seddo eiusmod tempor incididuntit.</p><span class="btn">View More</span></article>
  <article class="card"><div class="pic light" role="img" aria-label="Two colleagues reviewing documents"></div><h3>Sed pesru lorem ismciatin</h3><p>Lorem ipsum dolor sit amet, consectetur adicin elit, seddo eiusmod tempor incididuntit.</p><span class="btn">View More</span></article>
  <article class="card"><div class="pic warm" role="img" aria-label="Man checking phone on a city street at sunset"></div><h3>Sed pesru lorem ismciatin</h3><p>Lorem ipsum dolor sit amet, consectetur adicin elit, seddo eiusmod tempor incididuntit.</p><span class="btn">View More</span></article>
</div>
<div class="rule" style="top:969px"></div>

<h2 class="sec-head green" style="top:1011px">Business</h2>
<div class="arrows" style="top:1009px"><svg width="38" height="22" viewBox="0 0 38 22"><polyline points="12,3 4,11 12,19" fill="none" stroke="#999" stroke-width="2"/><polyline points="26,3 34,11 26,19" fill="none" stroke="#999" stroke-width="2"/></svg></div>
<div class="row" style="top:1060px">
  <article class="card"><div class="pic light" role="img" aria-label="Desk with charts, laptop and plant"></div><h3>Sed pesru lorem ismciatin</h3><p>Lorem ipsum dolor sit amet, consectetur adipiscn elit, seddo eiusmod tempor incididuntit.</p><span class="btn">View More</span></article>
  <article class="card"><div class="pic dark" role="img" aria-label="Businesswoman shaking hands"></div><h3>Sed pesru lorem ismciatin</h3><p>Lorem ipsum dolor sit amet, consectetur adicin elit, seddo eiusmod tempor incididuntit.</p><span class="btn">View More</span></article>
  <article class="card"><div class="pic" role="img" aria-label="Audience at a business seminar"></div><h3>Sed pesru lorem ismciatin</h3><p>Lorem ipsum dolor sit amet, consectetur adicin elit, seddo eiusmod tempor incididuntit.</p><span class="btn">View More</span></article>
</div>

<section class="band grey" style="top:1395px;height:549px"></section>
<h2 class="sec-head orange" style="top:1446px">Editor’s Picks</h2>
<div class="photo cool" style="left:160px;top:1493px;width:555px;height:374px" role="img" aria-label="Hands working on a laptop with a pen">
  <div class="play" style="left:242px;top:157px"><svg width="20" height="24" viewBox="0 0 20 24"><polygon points="2,0 20,12 2,24" fill="#fff"/></svg></div>
</div>
<aside class="list-panel" style="left:745px;top:1493px;width:293px;height:374px">
  <div class="head" style="background:var(--orange)">Latest Business News</div>
  <div class="item" style="top:66px"><span class="num" style="background:var(--orange)">01</span>Lorem ipsum dolor sit aconse ctetur adicrssum dolor sum.</div>
  <div class="divider" style="top:124px"></div>
  <div class="item" style="top:142px"><span class="num" style="background:var(--orange)">02</span>Lorem ipsum dolor sit aconse ctetur adicrssum dolor sum.</div>
  <div class="divider" style="top:203px"></div>
  <div class="item" style="top:225px"><span class="num" style="background:var(--orange)">03</span>Lorem ipsum dolor sit aconse ctetur adicrssum dolor sum.</div>
  <div class="divider" style="top:288px"></div>
  <div class="item" style="top:310px"><span class="num" style="background:var(--orange)">04</span>Lorem ipsum dolor sit aconse ctetur adicrssum dolor sum.</div>
</aside>

<h2 class="sec-head blue" style="top:2008px">Tech</h2>
<div class="arrows" style="top:2006px"><svg width="38" height="22" viewBox="0 0 38 22"><polyline points="12,3 4,11 12,19" fill="none" stroke="#999" stroke-width="2"/><polyline points="26,3 34,11 26,19" fill="none" stroke="#999" stroke-width="2"/></svg></div>
<div class="row four" style="top:2053px">
  <article class="card"><div class="pic" style="background:linear-gradient(135deg,#6c7fd0,#2a2f5a)" role="img" aria-label="Laptop with glowing data graphics"></div><h3>Sed pesru loreciatin</h3><p>Lorem ipsum dolor sit amet, conset etur adipiscneli seddo eiusmodtem por incididuntit.</p><span class="btn">View More</span></article>
  <article class="card"><div class="pic light" role="img" aria-label="Hands typing on a laptop in an office"></div><h3>Sed pesru loreciatin</h3><p>Lorem ipsum dolor sit amet, conset etur adipiscneli seddo eiusmodtem por incididuntit.</p><span class="btn">View More</span></article>
  <article class="card"><div class="pic dark" role="img" aria-label="Man in front of a chalkboard with tech doodles"></div><h3>Sed pesru loreciatin</h3><p>Lorem ipsum dolor sit amet, conset etur adipiscneli seddo eiusmodtem por incididuntit.</p><span class="btn">View More</span></article>
  <article class="card"><div class="pic warm" role="img" aria-label="Multimeter testing electronics"></div><h3>Sed pesru loreciatin</h3><p>Lorem ipsum dolor sit amet, conset etur adipiscneli seddo eiusmodtem por incididuntit.</p><span class="btn">View More</span></article>
</div>
<div class="rule" style="top:2416px"></div>

<h2 class="sec-head" style="top:2456px">Current Affairs</h2>
<div class="arrows" style="top:2454px"><svg width="38" height="22" viewBox="0 0 38 22"><polyline points="12,3 4,11 12,19" fill="none" stroke="#999" stroke-width="2"/><polyline points="26,3 34,11 26,19" fill="none" stroke="#999" stroke-width="2"/></svg></div>
<div class="row" style="top:2505px">
  <article class="card"><div class="pic light" role="img" aria-label="Glasses resting on a newspaper beside a cup"></div><h3>Sed pesru lorem ismciatin</h3><p>Lorem ipsum dolor sit amet, consectetur adipiscn elit, seddo eiusmod tempor incididuntit.</p><span class="btn">View More</span></article>
  <article class="card"><div class="pic warm" role="img" aria-label="Friends looking at phones in a cafe"></div><h3>Sed pesru lorem ismciatin</h3><p>Lorem ipsum dolor sit amet, consectetur adicin elit, seddo eiusmod tempor incididuntit.</p><span class="btn">View More</span></article>
  <article class="card"><div class="pic light" role="img" aria-label="Hand holding a smartphone with app icons"></div><h3>Sed pesru lorem ismciatin</h3><p>Lorem ipsum dolor sit amet, consectetur adicin elit, seddo eiusmod tempor incididuntit.</p><span class="btn">View More</span></article>
</div>

<section class="band grey" style="top:2862px;height:872px"></section>
<h2 class="sec-head green" style="top:2922px">More from around the Halvern News</h2>
<aside class="list-panel" style="left:160px;top:2982px;width:295px;height:374px">
  <div class="head" style="background:var(--red)">Feature News</div>
  <div class="item" style="top:70px"><span class="num" style="background:var(--red)">01</span>Lorem ipsum dolor sit aconse ctetur adicrssum dolor sum.</div>
  <div class="divider" style="top:126px"></div>
  <div class="item" style="top:146px"><span class="num" style="background:var(--red)">02</span>Lorem ipsum dolor sit aconse ctetur adicrssum dolor sum.</div>
  <div class="divider" style="top:206px"></div>
  <div class="item" style="top:229px"><span class="num" style="background:var(--red)">03</span>Lorem ipsum dolor sit aconse ctetur adicrssum dolor sum.</div>
  <div class="divider" style="top:290px"></div>
  <div class="item" style="top:312px"><span class="num" style="background:var(--red)">04</span>Lorem ipsum dolor sit aconse ctetur adicrssum dolor sum.</div>
</aside>
<div class="photo warm" style="left:485px;top:2982px;width:553px;height:374px" role="img" aria-label="Colleagues talking around a cafe table">
  <div class="play" style="left:240px;top:157px"><svg width="20" height="24" viewBox="0 0 20 24"><polygon points="2,0 20,12 2,24" fill="#fff"/></svg></div>
</div>
<div class="row" style="top:3386px">
  <article class="mcard"><div class="pic photo warm" style="position:relative" role="img" aria-label="Smiling businesswoman portrait"></div><div class="body"><h4>Lorem ipsmiciatisnde</h4><p>Lorem ipsum dolor sit alorm cect etur adipiscing elit, sed do ei.</p><div class="tag">NEWS</div></div></article>
  <article class="mcard"><div class="pic photo warm" style="position:relative" role="img" aria-label="Team gathered in an office"></div><div class="body"><h4>Lorem ipsmiciatisnde</h4><p>Lorem ipsum dolor sit alorm cect etur adipiscing elit, sed do ei.</p><div class="tag">BUSINESS</div></div></article>
  <article class="mcard"><div class="pic photo light" style="position:relative" role="img" aria-label="Businessman working at a laptop"></div><div class="body"><h4>Lorem ipsmiciatisnde</h4><p>Lorem ipsum dolor sit alorm cect etur adipiscing elit, sed do ei.</p><div class="tag">TECH</div></div></article>
  <article class="mcard"><div class="pic photo warm" style="position:relative" role="img" aria-label="Man in a suit in a city"></div><div class="body"><h4>Lorem ipsmiciatisnde</h4><p>Lorem ipsum dolor sit alorm cect etur adipiscing elit, sed do ei.</p><div class="tag">CURRENT AFFAIRS</div></div></article>
</div>

<h2 class="sec-head" style="top:3787px">Top Stories</h2>
<h2 class="sec-head green" style="top:3787px;left:763px">Featured Sections</h2>
<div class="row" style="top:3834px;width:577px">
  <article class="card"><div class="pic" role="img" aria-label="Group discussion in a meeting room"></div><h3>Sed pesru lorem ismciatin</h3><p>Lorem ipsum dolor sit amet, consectetur adipiscn elit, seddo eiusmod tempor incididuntit.</p><span class="btn">View More</span></article>
  <article class="card"><div class="pic light" role="img" aria-label="Presentation at a whiteboard"></div><h3>Sed pesru lorem ismciatin</h3><p>Lorem ipsum dolor sit amet, consectetur adicin elit, seddo eiusmod tempor incididuntit.</p><span class="btn">View More</span></article>
</div>
<div class="row" style="top:4143px;width:577px">
  <article class="card"><div class="pic light" role="img" aria-label="Woman presenting to colleagues"></div><h3>Sed pesru lorem ismciatin</h3><p>Lorem ipsum dolor sit amet, consectetur adipiscn elit, seddo eiusmod tempor incididuntit.</p><span class="btn">View More</span></article>
  <article class="card"><div class="pic light" role="img" aria-label="Woman smiling at her desk"></div><h3>Sed pesru lorem ismciatin</h3><p>Lorem ipsum dolor sit amet, consectetur adicin elit, seddo eiusmod tempor incididuntit.</p><span class="btn">View More</span></article>
</div>
<div class="photo light" style="left:763px;top:3834px;width:275px;height:151px" role="img" aria-label="Team meeting in a bright office"></div>
<div class="feat-item" style="top:4002px"><h3>Sed pesru lorem ismciatin</h3><p>Lorem ipsum dolor sit amet, consectetur adicin elit, seddo eiusmod tempor incididuntit.</p></div>
<div class="feat-item" style="top:4096px"><h3>Sed pesru lorem ismciatin</h3><p>Lorem ipsum dolor sit amet, consectetur adicin elit, seddo eiusmod tempor incididuntit.</p></div>
<div class="feat-item" style="top:4196px"><h3>Sed pesru lorem ismciatin</h3><p>Lorem ipsum dolor sit amet, consectetur adicin elit, seddo eiusmod tempor incididuntit.</p></div>
<div class="feat-item" style="top:4301px;border-bottom:none"><h3>Sed pesru lorem ismciatin</h3><p>Lorem ipsum dolor sit amet, consectetur adicin elit, seddo eiusmod tempor incididuntit.</p><span class="btn">View More</span></div>

<footer class="band footer">
  <div class="f-head" style="left:160px">ABOUT US</div>
  <div class="f-text" style="left:160px;width:190px">Lorem ipsum dolor sit alorme cons ecteur adipiscing elit, sed doeremips um dolor sit alormet, consectetorem ipsum dolorsit amet isse potentiesq uam ante aliquet lacuse.</div>
  <div class="f-head" style="left:416px">OTHER LINKS</div>
  <div class="f-text" style="left:416px">Home<br>Contact Us<br>News<br>Business<br>Tech All News</div>
  <div class="f-head" style="left:568px">FOLLOW US</div>
  <div class="social"><span></span><span></span><span></span><span></span><span></span></div>
  <div class="f-head" style="left:752px">NEWSLETTER</div>
  <div class="f-text" style="left:752px;width:290px">Lorem ipsum dolor sit alormet, consectetur adipiscing elit, sed doorem ipsum dolor sit alormet, consectetu</div>
  <div class="email">Email Address:<div class="signup">SIGN UP</div></div>
  <div class="copy">Copyrights © 2017 Halvern News. All Rights Reserved.</div>
</footer>

</body>
</html>
```